Bildschirmwerbung  Einkommensteuererklärungen
Bildschirmwerbung Einkommensteuererklärungen
Zielgruppe
Einkommensteuererklärungen für Arbeitnehmer/Rentner
Aufgabenstellung
Bildschirmwerbung JPG 1920x1080 Pixel (16:9 Format)

```html
<!DOCTYPE html>
<html lang="de">
<head>
<meta charset="utf-8">
<title>Bildschirmwerbung Einkommensteuererklärung</title>
<link rel="stylesheet" href="https://fonts.googleapis.com/css2?family=Open+Sans:wght@300;400;700&display=swap">
<style>
  :root {
    --navy: #00589b;
    --sky: #5bb3e2;
    --yellow: #ffe014;
    --white: #ffffff;
    --stage-top: #dedede;
    --stage-bottom: #ffffff;
  }
  * { margin: 0; padding: 0; box-sizing: border-box; }
  html, body { width: 996px; height: 1200px; overflow: hidden; }
  body {
    position: relative;
    font-family: "Open Sans", sans-serif;
    background: linear-gradient(to bottom, var(--stage-top) 0%, #f3f3f3 50%, var(--stage-bottom) 100%);
  }
  .banner {
    position: absolute;
    left: 93px;
    width: 811px;
    height: 456px;
    overflow: hidden;
  }
  .banner--photo { top: 92px; }
  .banner--pattern { top: 631px; background: var(--navy); }
  .banner .layer { position: absolute; inset: 0; }

  /* Banner 1 */
  .photo {
    position: absolute; left: 0; top: 0; width: 811px; height: 373px;
    background:
      radial-gradient(ellipse 180px 230px at 190px 200px, #d8c3b3 0%, rgba(216,195,179,0) 70%),
      radial-gradient(ellipse 200px 260px at 560px 150px, #d9c0a0 0%, rgba(217,192,160,0) 75%),
      linear-gradient(to bottom, rgba(255,255,255,0) 55%, #2a3c5c 100%),
      linear-gradient(to right, #eef1f3 0%, #f4f4f4 40%, #e2d3c2 70%, #c9cfc3 100%);
  }
  .headline-box {
    position: absolute; left: 345px; top: 131px; width: 466px; height: 140px;
    background: var(--navy);
  }
  .headline-box .headline { position: absolute; left: 63px; top: 20px; }
  .headline { line-height: 1.2; }
  .headline .lead { display: block; font-weight: 300; color: var(--white); }
  .headline .key { display: block; font-weight: 700; color: var(--yellow); letter-spacing: -0.5px; }
  .banner--photo .headline .lead { font-size: 40px; }
  .banner--photo .headline .key { font-size: 41px; margin-top: -2px; }

  .web-top {
    position: absolute; right: 35px; top: 25px;
    font-size: 14px; font-weight: 700; color: var(--navy);
  }
  .claim-band {
    position: absolute; left: 0; top: 373px; width: 560px; height: 83px;
    background: var(--navy);
  }
  .claim {
    position: absolute; left: 0; top: 392px; width: 506px;
    text-align: center; font-size: 17px; line-height: 22px; color: var(--white);
  }
  .claim strong { color: var(--yellow); font-weight: 700; }

  .brand {
    position: absolute; color: var(--white);
    font-weight: 400; font-size: 14px; line-height: 15px;
    display: flex; align-items: center; gap: 8px;
  }
  .brand .mark { width: 14px; height: 14px; background: var(--white); border-radius: 50%; flex: none; }
  .banner--photo .brand { left: 617px; top: 398px; }

  /* Banner 2 */
  .grid-field {
    position: absolute; inset: 0;
    background:
      linear-gradient(105deg, var(--navy) 0%, var(--navy) 30%, rgba(0,88,155,0) 75%),
      linear-gradient(to bottom right, #0b6fae 0%, #1a8fd0 60%, #0d7cbf 100%);
  }
  .banner--pattern .headline { position: absolute; left: 73px; top: 100px; }
  .banner--pattern .headline .lead { font-size: 68px; line-height: 66px; }
  .banner--pattern .headline .key { font-size: 66px; line-height: 66px; letter-spacing: -0.5px; }
  .pill {
    position: absolute; left: 159px; top: 257px; width: 406px; height: 56px;
    border-radius: 28px; background: var(--yellow);
    display: flex; flex-direction: column; justify-content: center; align-items: center;
    color: var(--navy); font-size: 15px; line-height: 19px;
  }
  .pill strong { font-weight: 700; }
  .banner--pattern .brand { left: 636px; top: 381px; font-size: 12px; line-height: 13px; }
  .web-bottom {
    position: absolute; left: 636px; top: 415px; width: 135px; text-align: center;
    font-size: 11px; font-weight: 700; color: var(--white);
  }
</style>
</head>
<body>

  <section class="banner banner--photo">
    <div class="photo" role="img" aria-label="Foto: lächelnder Mann mit Brille im Beratungsgespräch, unscharfe Gesprächspartnerin im Vordergrund"></div>
    <svg class="layer" width="811" height="456" viewBox="0 0 811 456" aria-hidden="true">
      <polygon points="502,456 811,78 811,456" fill="var(--sky)"/>
    </svg>
    <div class="claim-band"></div>
    <svg class="layer" width="811" height="456" viewBox="0 0 811 456" aria-hidden="true">
      <polygon points="502,456 811,78 811,456" fill="var(--sky)"/>
    </svg>
    <div class="headline-box">
      <h1 class="headline"><span class="lead">Zeit für die</span><span class="key">Steuererklärung?</span></h1>
    </div>
    <p class="web-top">www.lohnhilfe-wismar.de</p>
    <p class="claim">Einfach machen lassen und<br><strong>Zeit für wichtigere Dinge haben.</strong></p>
    <div class="brand"><span class="mark"></span><span>Lohnsteuerring<br>Nord</span></div>
  </section>

  <section class="banner banner--pattern">
    <div class="grid-field" role="img" aria-label="Dekoratives Rastermuster aus blauen Kacheln in Perspektive"></div>
    <svg class="layer" width="811" height="456" viewBox="0 0 811 456" aria-hidden="true">
      <polygon points="482,456 811,237 811,456" fill="var(--sky)"/>
    </svg>
    <h2 class="headline"><span class="lead">Zeit für die</span><span class="key">Steuererklärung?</span></h2>
    <p class="pill"><span>Einfach machen lassen und</span><strong>Zeit für wichtigere Dinge haben.</strong></p>
    <div class="brand"><span class="mark"></span><span>Lohnsteuerring<br>Nord</span></div>
    <p class="web-bottom">www.lohnhilfe-wismar.de</p>
  </section>

</body>
</html>
```